Redesign of an insurance website

Attached is an insurance website that I need to redesign. Currently the website is too dark. I like for example www.brambleshield.com . Could you make the website lighter and change the structure a little so that it is more user friendly?

Industry/Entity Type

Insurance

Number of Pages Required

4 page

```html
<!DOCTYPE html>
<html lang="cs">
<head>
<meta charset="utf-8">
<title>Pokryto.cz – srovnání pojištění</title>
<link href="https://fonts.googleapis.com/css2?family=PT+Sans:wght@400;700&family=Jost:ital,wght@0,400;0,500;1,400&display=swap" rel="stylesheet">
<style>
:root{
  --navy:#1d426e;
  --navy-dark:#17375d;
  --blue:#1c8fe0;
  --blue-light:#35b3f5;
  --green:#56ad2e;
  --green-light:#68c23a;
  --ink:#1a1a1a;
  --grey-bg:#f4f4f4;
  --footer:#2c2c2c;
  --line:#cfd6dc;
}
*{box-sizing:border-box;margin:0;padding:0}
html,body{width:1200px;height:1191px;overflow:hidden}
body{position:relative;font-family:"Jost",sans-serif;color:var(--ink);background:#fff}
.abs{position:absolute}

/* header */
.site-header{position:absolute;left:0;top:0;width:1200px;height:104px;background:#fff;border-top:2px solid var(--navy)}
.brand{position:absolute;left:140px;top:42px;font:700 31px/1 "PT Sans",sans-serif;color:var(--navy);letter-spacing:.3px}
.social{position:absolute;top:9px;display:flex;gap:6px;left:724px}
.social span{width:21px;height:21px;border-radius:50%;display:block}
.account-bar{position:absolute;left:808px;top:0;width:250px;height:32px;background:var(--navy);clip-path:polygon(0 0,100% 0,96% 100%,4% 100%);display:flex;align-items:center;justify-content:center;gap:14px;color:#fff;font:400 12px "PT Sans",sans-serif}
.account-bar i{font-style:normal;opacity:.5}
.main-nav{position:absolute;top:61px;right:144px;display:flex;font:700 12.5px "PT Sans",sans-serif;letter-spacing:.3px}
.main-nav a{color:var(--ink);text-decoration:none;padding:0 24px;border-left:1px solid #ddd}
.main-nav a:first-child{border:0}
.main-nav a:last-child{padding-right:0}

/* hero */
.hero{position:absolute;left:0;top:104px;width:1200px;height:510px;background:radial-gradient(ellipse at 75% 30%,var(--blue-light),var(--blue) 45%,#0a5fae 100%);overflow:hidden}
.hero-photo{position:absolute;left:370px;top:95px;width:360px;height:415px;background:radial-gradient(ellipse at 50% 40%,#e9d2c0,#9db9d6 55%,rgba(60,110,170,0) 80%);border-radius:48% 48% 0 0}
.hero-title{position:absolute;left:142px;top:88px;font:700 33px/38px "PT Sans",sans-serif;color:#fff}
.benefits{position:absolute;left:142px;top:183px;list-style:none;color:#fff;font-size:14.5px}
.benefits li{height:31px;display:flex;align-items:center;gap:9px}

/* quote form */
.quote-card{position:absolute;left:726px;top:134px;width:331px;height:494px;background:#fff;box-shadow:0 14px 10px -8px rgba(0,0,0,.25)}
.quote-head{position:absolute;left:-8px;top:31px;width:319px;height:76px;background:var(--green);border-radius:0 4px 4px 0;color:#fff;text-align:center;font:700 24px/29px "PT Sans",sans-serif;padding-top:9px}
.field{position:absolute;left:19px;width:293px;height:32px;border:1px solid var(--line);border-radius:2px;font-size:12px;color:#444;padding:0 14px;display:flex;align-items:center}
.agree{position:absolute;left:25px;top:272px;display:flex;align-items:center;gap:6px;font-size:13px}
.agree .box{width:22px;height:22px;border:1px solid var(--line)}
.calc-btn{position:absolute;left:19px;top:305px;width:293px;height:39px;background:linear-gradient(var(--green-light),var(--green));color:#fff;font:700 14px/39px "PT Sans",sans-serif;text-align:center;border-radius:2px}
.other{position:absolute;left:19px;top:362px;color:var(--green);font-size:12.5px}
.types{position:absolute;left:0;top:392px;width:331px}
.type{position:absolute;width:70px;text-align:center;font-size:10.5px;line-height:11px}
.type .ic{width:46px;height:46px;border-radius:50%;background:var(--green);margin:0 auto 4px;display:flex;align-items:center;justify-content:center}
.type.active .ic{background:var(--navy)}

/* content */
.content{position:absolute;left:0;top:614px;width:1200px;height:394px;background:var(--grey-bg)}
.h2{position:absolute;font:700 17.5px "PT Sans",sans-serif;color:var(--navy)}
.puzzle{position:absolute;left:141px;top:113px;width:273px;height:226px;border-radius:4px;background:radial-gradient(circle at 52% 52%,#d9ecff,#3b6aa8 25%,#122a52 70%)}
.text{position:absolute;font-size:13px;line-height:21.7px;color:#222;text-align:justify}
.save-btn{position:absolute;left:438px;top:303px;width:137px;height:36px;background:var(--green);color:#fff;font:700 14px/36px "PT Sans",sans-serif;text-align:center}

/* newsletter */
.newsletter{position:absolute;left:0;top:1008px;width:1200px;height:95px;background:var(--navy)}
.newsletter h3{position:absolute;left:265px;top:34px;color:#fff;font:700 22px "PT Sans",sans-serif}
.nl-input{position:absolute;left:501px;top:26px;width:401px;height:43px;background:#fff;font:italic 12px/43px "Jost",sans-serif;color:#555;padding-left:18px}
.nl-btn{position:absolute;left:902px;top:26px;width:132px;height:43px;background:var(--green);color:#fff;font:700 15px/43px "PT Sans",sans-serif;text-align:center;letter-spacing:.5px}

/* footer */
.site-footer{position:absolute;left:0;top:1103px;width:1200px;height:88px;background:var(--footer);color:#fff}
.site-footer .brand{left:144px;top:30px;color:#fff}
.legal{position:absolute;right:140px;top:25px;text-align:right;font-size:13.5px;line-height:20px}
</style>
</head>
<body>

<header class="site-header">
  <div class="brand">POKRYTO.CZ</div>
  <div class="social"><span style="background:#3b5998"></span><span style="background:#1da1f2"></span><span style="background:#dd4b39"></span></div>
  <div class="account-bar"><span>➜ PRIHLASIT SE</span><i>|</i><span>REGISTROVAT</span></div>
  <nav class="main-nav"><a href="#">O NAS</a><a href="#">CASTE DOTAZY</a><a href="#">KONTAKT</a></nav>
</header>

<section class="hero">
  <div class="hero-photo" role="img" aria-label="Usmívající se pár ukazuje palce nahoru"></div>
  <h1 class="hero-title">Proc hledat pojisteni pres<br>pokryto.cz?</h1>
  <ul class="benefits">
    <li><svg width="15" height="15" viewBox="0 0 15 15"><rect x="1" y="3" width="11" height="11" fill="none" stroke="#6cc33b" stroke-width="1.5"/><path d="M3 8l3 3 8-9" fill="none" stroke="#6cc33b" stroke-width="2.2"/></svg>s námi najdete tu nejvýhodnější nabídku</li>
    <li><svg width="15" height="15" viewBox="0 0 15 15"><rect x="1" y="3" width="11" height="11" fill="none" stroke="#6cc33b" stroke-width="1.5"/><path d="M3 8l3 3 8-9" fill="none" stroke="#6cc33b" stroke-width="2.2"/></svg>zaručíme vám nejlepší cenu na trhu</li>
    <li><svg width="15" height="15" viewBox="0 0 15 15"><rect x="1" y="3" width="11" height="11" fill="none" stroke="#6cc33b" stroke-width="1.5"/><path d="M3 8l3 3 8-9" fill="none" stroke="#6cc33b" stroke-width="2.2"/></svg>stačí pár minut a můžete ušetřit tisíce</li>
    <li><svg width="15" height="15" viewBox="0 0 15 15"><rect x="1" y="3" width="11" height="11" fill="none" stroke="#6cc33b" stroke-width="1.5"/><path d="M3 8l3 3 8-9" fill="none" stroke="#6cc33b" stroke-width="2.2"/></svg>srovnáváme všechny pojišťovny</li>
    <li><svg width="15" height="15" viewBox="0 0 15 15"><rect x="1" y="3" width="11" height="11" fill="none" stroke="#6cc33b" stroke-width="1.5"/><path d="M3 8l3 3 8-9" fill="none" stroke="#6cc33b" stroke-width="2.2"/></svg>zařídíme vám všechny druhy pojištění</li>
    <li><svg width="15" height="15" viewBox="0 0 15 15"><rect x="1" y="3" width="11" height="11" fill="none" stroke="#6cc33b" stroke-width="1.5"/><path d="M3 8l3 3 8-9" fill="none" stroke="#6cc33b" stroke-width="2.2"/></svg>vše vyřídíte z pohodlí domova</li>
    <li><svg width="15" height="15" viewBox="0 0 15 15"><rect x="1" y="3" width="11" height="11" fill="none" stroke="#6cc33b" stroke-width="1.5"/><path d="M3 8l3 3 8-9" fill="none" stroke="#6cc33b" stroke-width="2.2"/></svg>nemusíte nikam chodit a ušetříte</li>
  </ul>
</section>

<aside class="quote-card">
  <div class="quote-head">Najděte nejvýhodnější<br>pojištění</div>
  <div class="field" style="top:133px">Jméno</div>
  <div class="field" style="top:177px">Pnmeni</div>
  <div class="field" style="top:222px">E-mail</div>
  <div class="agree"><span class="box"><svg width="22" height="22" viewBox="0 0 22 22"><path d="M4 11l5 5L21 1" fill="none" stroke="#1d426e" stroke-width="2.5"/></svg></span>Souhlas. s podmínkami pojistit</div>
  <div class="calc-btn">SPOCITAT CENU</div>
  <div class="other">Chcete pojistit neco jineho?</div>
  <div class="types">
    <svg class="abs" style="left:16px;top:17px" width="10" height="14" viewBox="0 0 10 14"><path d="M8 1L2 7l6 6" fill="none" stroke="#888" stroke-width="2"/></svg>
    <svg class="abs" style="left:307px;top:17px" width="10" height="14" viewBox="0 0 10 14"><path d="M2 1l6 6-6 6" fill="none" stroke="#888" stroke-width="2"/></svg>
    <div class="type active" style="left:22px"><div class="ic"><svg width="24" height="20" viewBox="0 0 24 20"><circle cx="6" cy="15" r="4" fill="none" stroke="#fff" stroke-width="2"/><circle cx="19" cy="15" r="4" fill="none" stroke="#fff" stroke-width="2"/><path d="M6 15l6-7h5l2 7M11 4h4" stroke="#fff" stroke-width="2" fill="none"/></svg></div>Havarijní<br>pojištění</div>
    <div class="type" style="left:94px"><div class="ic"><svg width="22" height="22" viewBox="0 0 22 22"><path d="M11 2v18M3 12l8-4 8 4M7 19l4-2 4 2" stroke="#fff" stroke-width="2.5" fill="none" transform="rotate(45 11 11)"/></svg></div>Cestovní<br>pojištění</div>
    <div class="type" style="left:170px"><div class="ic"><svg width="22" height="20" viewBox="0 0 22 20"><path d="M2 10L11 2l9 8M5 8v10h12V8" fill="none" stroke="#fff" stroke-width="2.2"/><rect x="9" y="12" width="4" height="6" fill="#fff"/></svg></div>Pojištění<br>domova</div>
    <div class="type" style="left:239px"><div class="ic"><svg width="24" height="20" viewBox="0 0 24 20"><path d="M5 9l2-6h10l2 6" fill="none" stroke="#fff" stroke-width="2"/><rect x="2" y="9" width="20" height="7" rx="2" fill="#fff"/><rect x="4" y="15" width="3" height="4" fill="#fff"/><rect x="17" y="15" width="3" height="4" fill="#fff"/></svg></div>Povinne<br>ruceni</div>
  </div>
</aside>

<main class="content">
  <h2 class="h2" style="left:141px;top:60px">UZAVŘELI JSTE V MINULOSTI NEVÝHODNOU POJISTKU? ZBAVTE SE JÍ!</h2>
  <div class="puzzle" role="img" aria-label="Ruka vkládá zářící dílek skládačky"></div>
  <p class="text" style="left:439px;top:110px;width:282px;letter-spacing:.4px">Lorem ipsum dolor sit amet, consectetuer adipiscing elit, sed diam nonummy nibh euismod tincidunt ut laoreet dolore magna aliquam erat volutpat. Ut wisi enim ad minim tationullamcorper suscipit lobortis nisl ut aliquip exeuismod tincidunt ut laoreet dolore magna aliquam erat volutpat. Ut wisi enim ad minim veniam, quis nostrud exerci tation ullamcorperad minim.</p>
  <div class="save-btn">CHCI UŠETŘIT</div>
  <h2 class="h2" style="left:759px;top:58px">JAK TO FUNGUJE</h2>
  <p class="text" style="left:759px;top:110px;width:298px">Lorem ipsum dolor sit amet, consectetuer adipiscing elit, sed diam nonummy nibh euismod tincidunt ut laoreet dolore magna aliquam erat volutpat. Ut wisi enim ad minim tationullamcorper suscipit lobortis nisl ut aliquip exeuismod tincidunt ut laoreet dolore magna aliquam erat volutpat.</p>
</main>

<section class="newsletter">
  <svg class="abs" style="left:165px;top:30px" width="88" height="36" viewBox="0 0 88 36"><path d="M2 6h18M2 18h14M2 30h18" stroke="#fff" stroke-width="3"/><path d="M32 2h54l-8 32H24z" fill="none" stroke="#fff" stroke-width="3"/><path d="M32 2l22 18L86 2M24 34l20-16M78 34L62 18" fill="none" stroke="#fff" stroke-width="3"/></svg>
  <h3>ODEBÍRAT NEWSLEUER</h3>
  <div class="nl-input">Enter your email here</div>
  <div class="nl-btn">SUBSCRIBE</div>
</section>

<footer class="site-footer">
  <div class="brand">POKRYTO.CZ</div>
  <div class="legal">Ochrana soukromi | Podminky pouziti<br>Copyright 2017 Pokryto.CZ. Vsechna prava vyhrazena.</div>
</footer>

</body>
</html>
```